Business Card Design for a Technology Development Company

******* PLEASE NOTE (ALL DESIGNERS): I am going to finish the competition on Monday the 9th July (NOT SATURDAY 15TH). I have some designs I like and need to get them printed next week. Please submit any designs today or tomorrow. *******

PLEASE READ ALL OF THE REQUIREMENTS!!! I've rejected lot's of designs in the past because they didn't read the basic requirements - thanks and good luck!

Quill Harbor is a UK technology / small holding company that invests in startups and develops new ideas. In addition it provides IT Professional Services.

Ideally the design will be simple, professional, smart, and sophisticated, and overall be nice to look at. You can be creative as you like with the design, equally as simple as you like - you guys are the professionals so I'll leave it to your inspiration (make sure you incorporate the logo)!
Updates

PLEASE NOTE (ALL DESIGNERS): I am going to finish the competition on Monday the 9th July (NOT SATURDAY 15TH).  I have some designs I like and need to get them printed next week.  Please submit any designs today or tomorrow.

Target Market(s)

Enterprises / corporations / public sector / technical engineers / investors. More www.brantelix.com / www.vornel.com than www.pibbleroo.com!

Industry/Entity Type

Business

Requirements
Must have
• It should be modern and any artwork (if used) should be simple
- Pastel colours, dark and light colours, and shades are preferred over bright colours
- The design should incorporate the attached Quill Harbor logo and the logo colour scheme
- The logo should be on both sides. The back should just have the logo, maybe with some additional graphics
- It must have the following information on:

FirstName SecondName
Company Position
Email: name@quillharbor.co.uk
Mobile: +44 (0) 7700 984312

- The final design should be for a UK business card, dimensions: 85mm × 55mm
- The final design should have bleed marks to allow for printing and should be given in vector formats (EPS and AI)
Nice to have
• The Logo can be separated from the font in the logo on the front of the card. This isn't necessary or required, just to know it's not a limitation.
Should not have
• No bright colours (I prefer pastel colours, dark and light colours, and shades)
- Fonts that are to thin
- Effects or designs that make it difficult to print
- Italic or old fashioned looking fonts, i.e. anything like Times New Roman is a NO!

```html
<!DOCTYPE html>
<html lang="en">
<head>
<meta charset="utf-8">
<title>Quill Harbor – Business Card</title>
<link rel="stylesheet" href="https://fonts.googleapis.com/css2?family=Open+Sans:wght@400;600;700&display=swap">
<style>
  :root {
    --teal: #1c8896;
    --teal-dark: #136f7b;
    --aqua: #8ccfdc;
    --ink: #1f2a2e;
    --paper: #ffffff;
    --backdrop: #e9eef0;
  }
  * { margin: 0; padding: 0; box-sizing: border-box; }
  html, body {
    width: 1200px; height: 960px; overflow: hidden;
    background: var(--backdrop);
    font-family: "Open Sans", Arial, sans-serif;
  }
  .sheet {
    width: 1200px; height: 960px;
    display: flex; align-items: center; justify-content: center; gap: 60px;
  }
  .card {
    position: relative;
    width: 520px; height: 336px;
    overflow: hidden;
    box-shadow: 0 8px 24px rgba(20, 60, 70, 0.18);
  }
  .card__band {
    position: absolute; left: 0; right: 0; bottom: 0;
    height: 20px; background: var(--aqua);
  }
  .card__band-mark {
    position: absolute; bottom: 0; height: 20px; width: 22px;
  }
  .card__band-mark--light { right: 42px; background: var(--paper); }
  .card__band-mark--dark { right: 20px; background: var(--teal-dark); }

  /* Back */
  .card--back { background: var(--teal); }
  .card--back .wordmark {
    position: absolute; right: 34px; bottom: 62px;
    color: var(--paper); font-size: 44px; font-weight: 400; letter-spacing: -0.5px;
  }

  /* Front */
  .card--front { background: var(--paper); }
  .brand {
    position: absolute; left: 34px; top: 30px;
    display: flex; align-items: center; gap: 12px;
  }
  .brand__square { width: 30px; height: 30px; background: var(--teal); }
  .brand__name { color: var(--teal); font-size: 34px; font-weight: 400; letter-spacing: 0.5px; line-height: 1; }
  .person {
    position: absolute; left: 34px; top: 96px;
    color: var(--ink); font-size: 17px; font-weight: 600; line-height: 1.15;
  }
  .person__surname { color: var(--teal); }
  .divider {
    position: absolute; left: 34px; top: 160px;
    width: 250px; height: 2px; background: var(--teal);
  }
  .contact {
    position: absolute; left: 34px; top: 190px;
    list-style: none; font-size: 15px; font-weight: 600; color: var(--ink); line-height: 1.3;
  }
  .contact__label { display: inline-block; width: 26px; color: var(--teal); }
</style>
</head>
<body>
  <main class="sheet">
    <section class="card card--back" aria-label="Card back">
      <p class="wordmark">Quill Harbor</p>
      <div class="card__band"></div>
      <span class="card__band-mark card__band-mark--light"></span>
      <span class="card__band-mark card__band-mark--dark"></span>
    </section>

    <section class="card card--front" aria-label="Card front">
      <div class="brand">
        <span class="brand__square"></span>
        <span class="brand__name">Quill Harbor</span>
      </div>
      <p class="person">
        FirstName <span class="person__surname">SecondName</span><br>
        Company Position
      </p>
      <div class="divider"></div>
      <ul class="contact">
        <li><span class="contact__label">e:</span> name@quillharbor.co.uk</li>
        <li><span class="contact__label">m:</span> +44 (0) 7700 984312</li>
        <li><span class="contact__label">w:</span> www.quillharbor.co.uk</li>
      </ul>
      <div class="card__band"></div>
      <span class="card__band-mark card__band-mark--light"></span>
      <span class="card__band-mark card__band-mark--dark"></span>
    </section>
  </main>
</body>
</html>
```